Pest Control Business Card Design

I would like a business card designed for a professional, modern pest control business based in Rockhampton, Australia, called Harbour Ridge Termite & Pest Solutions. We provide high quality, affordable services to residential and commercial clients. Please refer to the attached PDF for details of what information to include on the card and the colour code of the existing logo. Please do not use cartoons or gimmicky graphics. We plan to print through Cardwell Press AU, and a template is included in the attached files. Thanks.

```html
<!DOCTYPE html>
<html lang="en">
<head>
<meta charset="utf-8">
<title>Harbour Ridge Termite &amp; Pest Solutions – Business Card</title>
<link href="https://fonts.googleapis.com/css2?family=Arimo:wght@400;700&display=swap" rel="stylesheet">
<style>
  :root {
    --bg: #d9d9d9;
    --card: #1f1e1e;
    --edge: #d9481a;
    --accent: #f05a22;
    --text: #f2f2f2;
    --muted: #e4e4e4;
  }
  * { box-sizing: border-box; margin: 0; padding: 0; }
  html, body {
    width: 1200px; height: 800px; overflow: hidden;
    background: var(--bg);
    font-family: "Arimo", Arial, sans-serif;
  }
  .canvas {
    width: 1200px; height: 800px;
    display: flex; flex-direction: column;
    align-items: center; justify-content: center;
    gap: 60px;
  }
  .card {
    position: relative;
    width: 560px; height: 320px;
    background: var(--card);
    border-radius: 22px;
    box-shadow: 0 4px 0 var(--edge), 0 14px 28px rgba(0,0,0,.25);
    color: var(--text);
    overflow: hidden;
  }
  .brand {
    display: flex; align-items: center; gap: 12px;
    font-weight: 700; color: var(--text);
    letter-spacing: .01em; line-height: 1.1;
  }
  .brand-mark {
    flex: none; background: var(--accent);
  }
  .brand-name { text-transform: uppercase; }

  /* front */
  .card-front .brand {
    position: absolute; left: 36px; top: 50%;
    transform: translateY(-50%); width: 250px;
    font-size: 20px;
  }
  .card-front .brand-mark { width: 16px; height: 16px; }
  .divider {
    position: absolute; left: 308px; top: 40px; bottom: 40px; width: 1px;
    background: linear-gradient(to bottom, rgba(255,255,255,0), rgba(255,255,255,.35) 30%, rgba(255,255,255,.35) 70%, rgba(255,255,255,0));
  }
  .contact {
    position: absolute; left: 332px; top: 70px;
    font-size: 13px; line-height: 1.45; color: var(--muted);
  }
  .contact-name { font-size: 21px; font-weight: 700; color: var(--text); }
  .contact-role { font-size: 14px; color: var(--accent); margin-bottom: 10px; }
  .contact-address { margin-bottom: 12px; }
  .contact-line { display: flex; align-items: center; gap: 8px; }
  .contact-line svg { width: 11px; height: 11px; flex: none; }

  /* back */
  .card-back .brand {
    position: absolute; left: 50%; top: 50%;
    transform: translate(-50%, -50%); width: 440px;
    font-size: 34px;
  }
  .card-back .brand-mark { width: 26px; height: 26px; }
</style>
</head>
<body>
<main class="canvas">
  <section class="card card-front" aria-label="Card front">
    <div class="brand">
      <span class="brand-mark"></span>
      <span class="brand-name">Harbour Ridge Termite &amp; Pest Solutions</span>
    </div>
    <div class="divider"></div>
    <div class="contact">
      <p class="contact-name">Liam Carver</p>
      <p class="contact-role">President</p>
      <p class="contact-address">42 Quarry Lane<br>Rockhampton, QLD 4700</p>
      <p class="contact-line">
        <svg viewBox="0 0 12 12" aria-hidden="true"><path fill="#f05a22" d="M2.5 1l2 2.2-1 1.3c.7 1.5 1.8 2.6 3.2 3.2l1.3-1 2.2 2-1 1.8C5.5 10.3 1.7 6.5 1 2z"/></svg>
        (07) 4920 3318
      </p>
      <p class="contact-line">
        <svg viewBox="0 0 12 12" aria-hidden="true"><rect x="1" y="2.5" width="10" height="7" fill="#f05a22"/><path d="M1 2.5l5 4 5-4" fill="none" stroke="#1f1e1e" stroke-width="1"/></svg>
        name@harbourridge.com
      </p>
      <p class="contact-line">
        <svg viewBox="0 0 12 12" aria-hidden="true"><circle cx="6" cy="6" r="5" fill="none" stroke="#f05a22" stroke-width="1.4"/><path d="M1 6h10M6 1c-2 2.5-2 7.5 0 10M6 1c2 2.5 2 7.5 0 10" fill="none" stroke="#f05a22" stroke-width="1"/></svg>
        www.harbourridge.com
      </p>
    </div>
  </section>

  <section class="card card-back" aria-label="Card back">
    <div class="brand">
      <span class="brand-mark"></span>
      <span class="brand-name">Harbour Ridge Termite &amp; Pest Solutions</span>
    </div>
  </section>
</main>
</body>
</html>
```